Frostvale Cool Packs needs stationery designed for their new logo

We have a new logo so now want all our stationery to be redesigned.
Frostvale is a gel ice pack product used by the seafood & food industry to transport chilled products around the world.

We would like to use our new logo with icy or snow backgrounds or elements.
Our company tag line is "Keep your products chilled for longer"
I'll attach our old business cards so that you can use the text off them.
2nd attachment is our new logo to be used.

We want a design for:
- Business cards
- Letter Head
- Email signature

Target Market(s)

seafood & chilled food distributors

Industry/Entity Type

Industry

Font styles to use
Sans Serif

Colors
0492cd
85cae6
cee9f5

Requirements
Must have
• Our logo
Nice to have
• Snow or ice background or image incorporated somehow

```html
<!DOCTYPE html>
<html lang="en">
<head>
<meta charset="utf-8">
<title>Frostvale Cool Packs – Stationery</title>
<link rel="stylesheet" href="https://fonts.googleapis.com/css2?family=Jost:ital,wght@0,300;0,400;0,500;0,600;0,700;1,400&family=Nunito+Sans:ital,wght@0,400;0,700;0,800;1,400&display=swap">
<style>
:root{
  --blue:#0492cd;
  --blue-bright:#1fb8ea;
  --blue-mid:#85cae6;
  --blue-pale:#cee9f5;
  --blue-deep:#1a6fb5;
  --navy:#1d4f8c;
  --grey:#9a9a9a;
  --text:#6b7a86;
  --white:#ffffff;
  --stage:#eceff2;
}
*{margin:0;padding:0;box-sizing:border-box}
html,body{width:1200px;height:1200px;overflow:hidden;background:var(--stage)}
body{position:relative;font-family:"Jost",sans-serif;color:var(--text)}
.sheet{position:absolute;overflow:hidden;background:var(--white);box-shadow:0 3px 10px rgba(0,0,0,.18)}
.sheet svg.art{position:absolute;left:0;top:0;width:100%;height:100%}
.abs{position:absolute}

/* letterhead */
.letterhead{left:40px;top:50px;width:577px;height:816px;background:linear-gradient(180deg,#fff 0%,#eef8fd 60%,#fff 100%)}
.letterhead .tagline{left:200px;top:24px;font-size:14.5px;font-weight:600;color:var(--blue);letter-spacing:.3px}
.letterhead .brand{left:24px;top:70px;font-size:36px;font-weight:700;color:var(--white)}
.letterhead .section-title{left:70px;top:186px;font-size:27px;font-weight:400;color:var(--blue)}
.letterhead .contact{left:360px;top:180px;font-size:8.6px;font-weight:600;color:var(--blue);line-height:11px}
.contact .row{display:flex;gap:8px;margin-bottom:7px;align-items:flex-start}
.contact svg{width:10px;height:10px;flex:none;margin-top:1px}
.letterhead .headline{left:92px;top:298px;font-size:31px;font-weight:300;color:var(--blue);letter-spacing:.5px}
.letterhead .body-copy{left:93px;top:350px;width:400px;font-size:9.4px;line-height:13.6px;color:var(--text)}
.body-copy p{margin-bottom:14px}
.letterhead .sign-off{left:250px;top:572px;width:260px;text-align:right;font-size:9.4px;line-height:13.4px}
.sign-off .role{font-weight:700;color:#4a5660}
.sign-off .note{color:var(--blue)}
.sign-off .web{font-size:8.4px;color:var(--grey)}
.letterhead .person{right:14px;top:690px;text-align:left;color:var(--white)}
.person .name{font-family:"Nunito Sans",sans-serif;font-weight:800;font-size:18.5px;line-height:22px}
.person .title{font-style:italic;font-size:12px;letter-spacing:.3px}
.letterhead .footer-contact{left:307px;top:776px;font-size:11.5px;color:var(--blue);line-height:18px}
.footer-contact .row{display:flex;gap:6px;align-items:center}
.footer-contact svg{width:11px;height:11px}
.footer-contact .web{font-family:"Nunito Sans",sans-serif;font-weight:800;letter-spacing:.6px}

/* card front */
.card-front{left:645px;top:158px;width:497px;height:284px}
.card-front .brand{left:110px;top:52px;font-size:58px;font-weight:700;color:var(--white);letter-spacing:.5px}
.card-front .mark{left:60px;top:76px;width:40px;height:40px;border-radius:50%;background:var(--navy)}
.card-front .tagline{left:86px;top:134px;font-size:15px;font-weight:600;color:var(--white);letter-spacing:.2px}

/* card back */
.card-back{left:645px;top:471px;width:503px;height:287px}
.card-back .name{left:10px;top:136px;font-family:"Nunito Sans",sans-serif;font-size:30px;font-weight:800;color:var(--blue-deep)}
.card-back .title{left:13px;top:178px;font-size:19px;font-style:italic;color:var(--blue-deep);letter-spacing:.3px}
.card-back .divider{left:233px;top:120px;width:1px;height:180px;background:linear-gradient(180deg,transparent,#dfe4e8,transparent)}
.card-back .contact-list{left:250px;top:172px;font-size:12.5px;color:var(--blue-deep);line-height:20px}
.contact-list .row{display:flex;gap:12px;align-items:center;margin-bottom:10px}
.contact-list svg{width:20px;height:18px;flex:none}
.contact-list .web{font-family:"Nunito Sans",sans-serif;font-weight:800;letter-spacing:.8px;font-size:13.5px}

/* email signature */
.email-signature{left:226px;top:903px;width:752px;height:253px}
.email-signature .rule{left:0;width:100%;height:2px}
.rule.blue{background:var(--blue-deep)}
.rule.grey{background:#b5b9bd}
.email-signature .brand{left:100px;top:96px;font-size:52px;font-weight:700;color:var(--grey)}
.email-signature .mark{left:40px;top:110px;width:44px;height:44px;border-radius:50%;background:var(--blue-deep)}
.email-signature .divider{left:376px;top:55px;width:1px;height:150px;background:linear-gradient(180deg,transparent,#d4d9dd,transparent)}
.email-signature .name{left:380px;top:48px;width:372px;text-align:center;font-family:"Nunito Sans",sans-serif;font-size:35px;font-weight:800;color:var(--blue-deep)}
.email-signature .title{left:380px;top:98px;width:372px;text-align:center;font-size:19px;font-style:italic;color:var(--blue-deep);letter-spacing:.3px}
.email-signature .contact-list{left:412px;top:156px;color:var(--blue-deep)}
.email-signature .contact-list .row{margin-bottom:4px;gap:14px}
.email-signature .contact-list svg{width:26px;height:24px}
.email-signature .web{font-size:21px;letter-spacing:1.6px}
.email-signature .mail{font-size:14.5px;letter-spacing:.6px}
</style>
</head>
<body>

<svg width="0" height="0" style="position:absolute">
  <defs>
    <linearGradient id="iceStrip" x1="0" y1="0" x2="1" y2="1">
      <stop offset="0" stop-color="#cfe6f3"/>
      <stop offset=".5" stop-color="#e8f4fa"/>
      <stop offset="1" stop-color="#b9dcef"/>
    </linearGradient>
    <linearGradient id="bandBlue" x1="0" y1="0" x2="1" y2="0">
      <stop offset="0" stop-color="#1fb8ea"/>
      <stop offset=".55" stop-color="#85cae6"/>
      <stop offset="1" stop-color="#1fb8ea"/>
    </linearGradient>
    <linearGradient id="iceBlock" x1="0" y1="0" x2="1" y2="1">
      <stop offset="0" stop-color="#6fc3ee"/>
      <stop offset=".45" stop-color="#2aa3e3"/>
      <stop offset="1" stop-color="#1b7fd0"/>
    </linearGradient>
    <symbol id="icon-mail" viewBox="0 0 20 14"><rect x="1" y="1" width="18" height="12" fill="currentColor"/><path d="M1 1 L10 8 L19 1 M1 13 L8 7 M19 13 L12 7" stroke="#fff" stroke-width="1.4" fill="none"/></symbol>
    <symbol id="icon-globe" viewBox="0 0 20 20"><circle cx="10" cy="10" r="8.5" fill="none" stroke="currentColor" stroke-width="2"/><ellipse cx="10" cy="10" rx="3.5" ry="8.5" fill="none" stroke="currentColor" stroke-width="1.5"/><path d="M2 10 H18 M4 5.5 H16 M4 14.5 H16" stroke="currentColor" stroke-width="1.3"/></symbol>
    <symbol id="icon-pin" viewBox="0 0 12 16"><path d="M6 1 C2.5 1 1 3.5 1 6 C1 9.5 6 15 6 15 C6 15 11 9.5 11 6 C11 3.5 9.5 1 6 1Z" fill="none" stroke="currentColor" stroke-width="2"/><circle cx="6" cy="6" r="1.8" fill="currentColor"/></symbol>
    <symbol id="icon-phone" viewBox="0 0 16 16"><path d="M3 1 L6 1 L7 5 L5 6.5 C6 9 7 10 9.5 11 L11 9 L15 10 L15 13 C15 14 14 15 13 15 C6 15 1 10 1 3 C1 2 2 1 3 1Z" fill="currentColor"/></symbol>
  </defs>
</svg>

<!-- Letterhead -->
<section class="sheet letterhead">
  <svg class="art" viewBox="0 0 577 816" preserveAspectRatio="none">
    <path d="M0,0 L577,0 L577,28 C430,72 250,58 0,0 Z" fill="#ffffff"/>
    <path d="M0,0 C220,60 420,75 577,28 L577,50 C430,140 220,150 0,150 Z" fill="url(#bandBlue)"/>
    <path d="M0,0 L0,150 L0,0 Z" fill="var(--blue-bright)"/>
    <path d="M0,0 C60,15 90,22 120,28 L0,28 Z" fill="var(--blue-bright)"/>
    <path role="img" aria-label="Icy frost texture strip" d="M0,150 C220,150 430,140 577,50 L577,75 C440,170 220,190 0,176 Z" fill="url(#iceStrip)"/>
    <path role="img" aria-label="Icy frost texture strip" d="M0,745 C150,680 380,640 577,636 L577,680 C350,676 150,710 0,770 Z" fill="url(#iceStrip)"/>
    <path d="M0,770 C150,710 350,676 577,680 L577,800 C420,765 200,770 0,815 Z" fill="url(#bandBlue)"/>
  </svg>
  <div class="abs tagline">KEEP YOUR PRODUCTS CHILLED FOR LONGER</div>
  <div class="abs brand">Frostvale</div>
  <div class="abs section-title">LOREM IPSUM</div>
  <div class="abs contact">
    <div class="row"><svg style="color:var(--blue)"><use href="#icon-mail"/></svg><span>info@frostvale.com.au</span></div>
    <div class="row"><svg style="color:var(--blue)"><use href="#icon-pin"/></svg><span>P.O. Box 418<br>Harbour Road, Hobart, AU</span></div>
    <div class="row"><svg style="color:var(--blue)"><use href="#icon-phone"/></svg><span>+61 3 5550 1427<br>+61 3 5550 8863</span></div>
  </div>
  <div class="abs headline">HEADLINE</div>
  <div class="abs body-copy">
    <p>Lorem ipsum dolor sit amet, consectetur adipiscing elit. Fusce dignissim pretium consectetur. Curabitur tempor posuere massa in varius. Pellentesque viverra nibh eu vehicula mattis. Nullam porta facilisis justo, a feugiat dolor sodales sed. Vestibulum neque nisi, elementum tincidunt metus sit amet, egestas bibendum enim. Aenean a blandit elit, vel rutrum mi. Nunc dapibus turpis sed massa aliquet tincidunt.</p>
    <p>Pellentesque id neque ligula. Nullam posuere, ligula a mattis posuere, lacus nisl adipiscing nunc, eu congue justo est ut diam. Nam quam nibh, dignissim non consequat in, semper eget purus. Nulla arcu sapien, viverra vitae metus tempor, congue ornare diam.</p>
    <p>Pellentesque vel nibh tempus, ullamcorper tortor sed, bibendum augue. Phasellus sollicitudin justo et quam aliquam sollicitudin. Sed eget nibh mollis, mattis sem et, viverra nulla.</p>
  </div>
  <div class="abs sign-off">
    <div class="role">Creative Art Director</div>
    <div class="note">Pellentesque id neque ligula. Nullam posuere</div>
    <div class="web">www.frostvale.com.au</div>
  </div>
  <div class="abs person">
    <div class="name">Darren Hollis</div>
    <div class="title">Business Development</div>
  </div>
  <div class="abs footer-contact">
    <div class="row"><svg><use href="#icon-mail"/></svg><span>darren.hollis@frostvale.com.au</span></div>
    <div class="row"><svg><use href="#icon-globe"/></svg><span class="web">www.frostvale.com.au</span></div>
  </div>
</section>

<!-- Business card front -->
<section class="sheet card-front">
  <svg class="art" viewBox="0 0 497 284" preserveAspectRatio="none">
    <rect role="img" aria-label="Cracked blue ice background" width="497" height="284" fill="url(#iceBlock)"/>
    <path d="M0,230 C120,170 260,160 497,215 L497,262 C300,220 120,215 0,275 Z" fill="#e9f3f8"/>
    <path d="M0,218 C120,165 260,150 497,200 L497,258 C320,215 150,200 0,245 Z" fill="url(#bandBlue)"/>
    <path d="M0,284 C150,230 320,230 497,262 L497,284 Z" fill="var(--navy)"/>
  </svg>
  <div class="abs mark"></div>
  <div class="abs brand">Frostvale</div>
  <div class="abs tagline">KEEP YOUR PRODUCTS CHILLED FOR LONGER</div>
</section>

<!-- Business card back -->
<section class="sheet card-back">
  <svg class="art" viewBox="0 0 503 287" preserveAspectRatio="none">
    <path d="M0,60 C120,90 240,10 320,5 C400,0 460,40 503,72 L503,62 C450,20 380,5 300,8 C220,12 120,70 0,50 Z" fill="#b8e0f2"/>
    <path d="M0,72 C140,80 260,8 360,10 C430,12 480,50 503,72 L0,150 Z" fill="url(#bandBlue)"/>
    <path d="M0,150 L503,72 L503,80 C460,60 420,40 360,40 C250,42 140,130 0,120 Z" fill="#ffffff"/>
    <rect role="img" aria-label="Pale frosted ice strip" x="0" y="240" width="503" height="47" fill="url(#iceStrip)"/>
  </svg>
  <div class="abs name">Darren Hollis</div>
  <div class="abs title">Business Development</div>
  <div class="abs divider"></div>
  <div class="abs contact-list">
    <div class="row"><svg><use href="#icon-globe"/></svg><span class="web">www.frostvale.com.au</span></div>
    <div class="row"><svg><use href="#icon-mail"/></svg><span>darren.hollis@frostvale.com.au</span></div>
  </div>
</section>

<!-- Email signature -->
<section class="sheet email-signature">
  <div class="abs rule grey" style="top:26px"></div>
  <div class="abs rule blue" style="top:32px"></div>
  <div class="abs rule blue" style="top:220px"></div>
  <div class="abs rule grey" style="top:226px"></div>
  <div class="abs mark"></div>
  <div class="abs brand">Frostvale</div>
  <div class="abs divider"></div>
  <div class="abs name">Darren Hollis</div>
  <div class="abs title">Business Development</div>
  <div class="abs contact-list">
    <div class="row"><svg><use href="#icon-globe"/></svg><span class="web">www.frostvale.com.au</span></div>
    <div class="row"><svg><use href="#icon-mail"/></svg><span class="mail">darren.hollis@frostvale.com.au</span></div>
  </div>
</section>

</body>
</html>
```